Linkmesa and Glimtoria advertising

We need Linkmesa and Glimtoria ads. Simple ad with Alaska themed background.
This ad is to introduce our new ZENIRO Internet service.
--Speeds to 500 mpbs
-- Packages start at only $89.99 for speeds to 100mbps
-- Fiber Optic based connection, Not satellite
-- Extreme low latency, consistent speeds
--FREE equipment, FREE Installation, FREE wifi router, First month of service FREE

```html
<!DOCTYPE html>
<html lang="en">
<head>
<meta charset="utf-8">
<title>ZENIRO Internet Service</title>
<link rel="stylesheet" href="https://fonts.googleapis.com/css2?family=Poppins:wght@400;500;600;700;800&family=Roboto+Condensed:wght@500&display=swap">
<style>
  :root {
    --sky-deep: #0b3a4c;
    --sky-teal: #127b86;
    --aurora: #2fe3da;
    --ground: #141a28;
    --white: #ffffff;
    --card-head: #f7f7fa;
    --purple: #3a1670;
    --cyan: #4cc6f5;
    --alert: #ff3b3b;
    --navy: #10172a;
    --card-body: rgba(22, 38, 58, 0.78);
  }
  * { margin: 0; padding: 0; box-sizing: border-box; }
  html, body { width: 1200px; height: 1200px; overflow: hidden; background: var(--ground); }
  .ad {
    position: relative; width: 1200px; height: 1200px; overflow: hidden;
    font-family: "Poppins", sans-serif; color: var(--white);
  }
  .backdrop {
    position: absolute; inset: 0;
    background:
      radial-gradient(ellipse 520px 260px at 620px 560px, rgba(47,227,218,0.55), transparent 70%),
      radial-gradient(ellipse 420px 220px at 1020px 330px, rgba(47,227,218,0.25), transparent 70%),
      linear-gradient(180deg, #0a2a3a 0%, var(--sky-deep) 18%, var(--sky-teal) 45%, #185d72 62%, #1b3447 76%, var(--ground) 92%);
  }
  .brand {
    position: absolute; left: 50px; top: 76px;
    font-weight: 600; font-size: 40px; line-height: 1; letter-spacing: -0.5px;
  }
  .intro { position: absolute; left: 0; top: 150px; width: 1200px; height: 110px; }
  .headline {
    position: absolute; left: 0; top: 252px; width: 1200px; text-align: center;
    font-weight: 700; font-size: 200px; line-height: 1; letter-spacing: -4px;
  }
  .subline {
    position: absolute; left: 0; top: 452px; width: 1200px; text-align: center;
    font-family: "Roboto Condensed", sans-serif; font-weight: 500; font-size: 84px; line-height: 1;
  }
  .cards { position: absolute; top: 793px; left: 57px; display: flex; gap: 29px; }
  .card { width: 249px; height: 194px; border-radius: 4px; overflow: hidden; background: var(--card-body); }
  .card-head {
    height: 50px; background: var(--card-head); color: var(--purple);
    font-weight: 600; font-size: 17px; display: flex; align-items: center; justify-content: center;
  }
  .card-body { height: 144px; display: flex; flex-direction: column; align-items: center; justify-content: center; text-align: center; line-height: 1; }
  .big-num { font-weight: 800; font-size: 62px; color: var(--cyan); }
  .unit { font-weight: 700; font-size: 40px; margin-top: -4px; }
  .price { font-weight: 800; font-size: 60px; color: var(--cyan); }
  .price sup { font-size: 24px; vertical-align: 28px; }
  .small { font-size: 18px; font-weight: 400; margin: 4px 0 6px; }
  .speed { font-weight: 800; font-size: 50px; }
  .speed span { font-size: 18px; font-weight: 700; }
  .feature { font-weight: 700; font-size: 28px; color: var(--cyan); line-height: 1; }
  .note { font-size: 18px; margin-top: 4px; }
  .alert { color: var(--alert); font-weight: 700; font-size: 18px; margin-top: 2px; }
  .perks { position: absolute; top: 1070px; left: 58px; list-style: none; display: grid; grid-template-columns: 299px auto; row-gap: 14px; }
  .perk { display: flex; align-items: center; gap: 18px; font-size: 25px; font-weight: 500; }
  .perk svg { flex: none; }
  .order { position: absolute; left: 795px; top: 1054px; width: 405px; height: 99px; }
  .order-label {
    position: absolute; left: 878px; top: 1054px; height: 99px; display: flex; align-items: center; gap: 14px;
    color: var(--navy); font-weight: 700; font-size: 40px;
  }
</style>
</head>
<body>
<main class="ad">
  <div class="backdrop" role="img" aria-label="Night landscape in Alaska: teal aurora and a shooting star over snowy mountains, a pine forest and a calm lake"></div>

  <div class="brand">Norvale Networks</div>

  <svg class="intro" viewBox="0 0 1200 110" aria-label="Introduce our new">
    <defs><path id="arc" d="M345 95 Q600 -5 855 95"/></defs>
    <text font-family="Poppins, sans-serif" font-size="32" font-weight="400" letter-spacing="8" fill="#fff" text-anchor="middle">
      <textPath href="#arc" startOffset="50%">INTRODUCE OUR NEW</textPath>
    </text>
    <g fill="#fff">
      <polygon points="0,-12 3.5,-4 12,-4 5,1 8,10 0,5 -8,10 -5,1 -12,-4 -3.5,-4" transform="translate(486 94)"/>
      <polygon points="0,-12 3.5,-4 12,-4 5,1 8,10 0,5 -8,10 -5,1 -12,-4 -3.5,-4" transform="translate(539 88)"/>
      <polygon points="0,-12 3.5,-4 12,-4 5,1 8,10 0,5 -8,10 -5,1 -12,-4 -3.5,-4" transform="translate(601 84)"/>
      <polygon points="0,-12 3.5,-4 12,-4 5,1 8,10 0,5 -8,10 -5,1 -12,-4 -3.5,-4" transform="translate(664 88)"/>
      <polygon points="0,-12 3.5,-4 12,-4 5,1 8,10 0,5 -8,10 -5,1 -12,-4 -3.5,-4" transform="translate(720 94)"/>
    </g>
  </svg>

  <h1 class="headline">ZENIRO</h1>
  <h2 class="subline">INTERNET SERVICE</h2>

  <section class="cards">
    <article class="card">
      <div class="card-head">Speeds to</div>
      <div class="card-body"><div class="big-num">500</div><div class="unit">mbps</div></div>
    </article>
    <article class="card">
      <div class="card-head">Packages start at only</div>
      <div class="card-body">
        <div class="price"><sup>$</sup>89<sup>.99</sup></div>
        <div class="small">for speeds to</div>
        <div class="speed">100<span>mbps</span></div>
      </div>
    </article>
    <article class="card">
      <div class="card-head">Connection</div>
      <div class="card-body">
        <div class="feature">FIBER OPTIC</div>
        <div class="note">based connection</div>
        <div class="alert">Not satellite</div>
      </div>
    </article>
    <article class="card">
      <div class="card-head">Consistent Speed</div>
      <div class="card-body">
        <div class="feature">EXTREME<br>LOW LATENCY</div>
        <div class="note">consistent speeds</div>
      </div>
    </article>
  </section>

  <ul class="perks">
    <li class="perk"><svg width="34" height="34" viewBox="0 0 34 34"><circle cx="17" cy="17" r="15" fill="none" stroke="#4cc6f5" stroke-width="2.5"/><path d="M10 17l5 5 9-10" fill="none" stroke="#4cc6f5" stroke-width="2.5" stroke-linecap="round" stroke-linejoin="round"/></svg>FREE equipment</li>
    <li class="perk"><svg width="34" height="34" viewBox="0 0 34 34"><circle cx="17" cy="17" r="15" fill="none" stroke="#4cc6f5" stroke-width="2.5"/><path d="M10 17l5 5 9-10" fill="none" stroke="#4cc6f5" stroke-width="2.5" stroke-linecap="round" stroke-linejoin="round"/></svg>FREE wifi router</li>
    <li class="perk"><svg width="34" height="34" viewBox="0 0 34 34"><circle cx="17" cy="17" r="15" fill="none" stroke="#4cc6f5" stroke-width="2.5"/><path d="M10 17l5 5 9-10" fill="none" stroke="#4cc6f5" stroke-width="2.5" stroke-linecap="round" stroke-linejoin="round"/></svg>FREE Installation</li>
    <li class="perk"><svg width="34" height="34" viewBox="0 0 34 34"><circle cx="17" cy="17" r="15" fill="none" stroke="#4cc6f5" stroke-width="2.5"/><path d="M10 17l5 5 9-10" fill="none" stroke="#4cc6f5" stroke-width="2.5" stroke-linecap="round" stroke-linejoin="round"/></svg>First month of service FREE</li>
  </ul>

  <svg class="order" viewBox="0 0 405 99" aria-hidden="true"><polygon points="74,0 405,0 405,99 0,99" fill="#fff"/></svg>
  <div class="order-label">ORDER NOW <svg width="26" height="30" viewBox="0 0 26 30"><polygon points="0,0 26,15 0,30" fill="#10172a"/></svg></div>
</main>
</body>
</html>
```